Brisk Comet- Energy shot - ....Amazing Energy for Amazing people

To design a creative /unique logo and picture for Brisk Comet Energy/ energy shot product similar to Nine Dawn energy shot...Berry flavor

I want the design to cover the entire bottle. in addition to Logo (Brisk Comet Energy )

So Brisk Comet Energy will be a competitor of Nine Dawn energy and I want a creative,fantastic, attractive design to catch customers eyes, the product will be in similar size 2oz bottle (see attached image). This template is based on a common 2oz bottle size that measures exactly 114mm circumference x 83mm-85mm height (including cap ).
Please include At the top cap a Logo for: Brisk Comet...

Target Market(s)

Young, busy professionals, athletics

Industry/Entity Type

Product

Logo Text

Vopra Energy...Amazing Energy &Taste !

Requirements
Must have
• Creative exciting design...Vopra Energy...Fan
Nice to have
• Be a genius....Be creative...Be Amazing !

```html
<!DOCTYPE html>
<html lang="en">
<head>
<meta charset="utf-8">
<title>Brisk Comet Energy Shots – Bottle Label</title>
<link href="https://fonts.googleapis.com/css2?family=Russo+One&family=Exo+2:wght@700&display=swap" rel="stylesheet">
<style>
  :root {
    --page-bg: #ffffff;
    --label-red: #b50f14;
    --label-red-dark: #7e0508;
    --label-red-glow: #ee2a30;
    --band-blue: #173b8c;
    --band-blue-dark: #0b1e55;
    --band-blue-light: #2f6fc4;
    --panel-navy: #0a1540;
    --stripe-silver: #d9dde3;
    --stripe-red: #e3151c;
    --text-white: #ffffff;
    --runner-blue: #2d7fe0;
  }
  html, body {
    margin: 0;
    padding: 0;
    width: 1200px;
    height: 957px;
    overflow: hidden;
    background: var(--page-bg);
  }
  .canvas {
    position: relative;
    width: 1200px;
    height: 957px;
  }
  .label {
    position: absolute;
    left: 674px;
    top: 78px;
    width: 397px;
    height: 774px;
    overflow: hidden;
  }
  .label-art {
    position: absolute;
    inset: 0;
    width: 397px;
    height: 774px;
  }
  .runner-figure {
    position: absolute;
    left: 32px;
    top: 318px;
    width: 78px;
    height: 118px;
    border-radius: 40px 40px 20px 20px;
    background: linear-gradient(180deg, var(--runner-blue), #1a4fa8);
    opacity: 0.85;
  }
  .brand-name {
    position: absolute;
    left: 118px;
    top: 268px;
    width: 250px;
    margin: 0;
    font-family: "Russo One", sans-serif;
    font-weight: 400;
    font-size: 66px;
    line-height: 76px;
    color: var(--text-white);
    text-align: center;
  }
  .product-type {
    position: absolute;
    left: 40px;
    top: 445px;
    width: 340px;
    height: 40px;
    margin: 0;
    font-family: "Russo One", sans-serif;
    font-size: 31px;
    line-height: 40px;
    letter-spacing: 1px;
    color: var(--text-white);
    text-align: center;
    white-space: nowrap;
    transform: rotate(-8.7deg);
    transform-origin: 50% 50%;
  }
  .product-details {
    position: absolute;
    left: 60px;
    top: 530px;
    width: 280px;
    margin: 0;
    font-family: "Exo 2", sans-serif;
    font-weight: 700;
    font-size: 22px;
    line-height: 35px;
    letter-spacing: 3px;
    color: var(--text-white);
    text-align: center;
  }
</style>
</head>
<body>
<main class="canvas">
  <section class="label" aria-label="Brisk Comet Energy Shots bottle label">
    <svg class="label-art" viewBox="0 0 397 774" aria-hidden="true">
      <defs>
        <radialGradient id="red-glow-top" cx="0.5" cy="0.1" r="0.55">
          <stop offset="0" stop-color="var(--label-red-glow)"/>
          <stop offset="0.6" stop-color="var(--label-red)"/>
          <stop offset="1" stop-color="var(--label-red-dark)"/>
        </radialGradient>
        <radialGradient id="red-glow-bottom" cx="0.5" cy="0.9" r="0.5">
          <stop offset="0" stop-color="var(--label-red-glow)" stop-opacity="0.9"/>
          <stop offset="1" stop-color="var(--label-red-glow)" stop-opacity="0"/>
        </radialGradient>
        <radialGradient id="band-glow" cx="0.55" cy="0.55" r="0.6">
          <stop offset="0" stop-color="var(--band-blue-light)"/>
          <stop offset="0.6" stop-color="var(--band-blue)"/>
          <stop offset="1" stop-color="var(--band-blue-dark)"/>
        </radialGradient>
        <linearGradient id="silver" x1="0" y1="0" x2="1" y2="0">
          <stop offset="0" stop-color="#ffffff"/>
          <stop offset="0.6" stop-color="var(--stripe-silver)"/>
          <stop offset="1" stop-color="#9aa1ab"/>
        </linearGradient>
      </defs>
      <rect class="label-base" width="397" height="774" fill="url(#red-glow-top)"/>
      <rect class="label-base-glow" width="397" height="774" fill="url(#red-glow-bottom)"/>
      <polygon class="blue-band" points="0,172 397,108 397,612 0,682" fill="url(#band-glow)"/>
      <path class="name-panel" d="M0,285 L378,223 L378,390 Q378,410 352,414 L0,472 Z" fill="var(--panel-navy)" opacity="0.92"/>
      <polygon class="silver-stripe" points="0,272 378,210 378,224 0,287" fill="url(#silver)"/>
      <polygon class="red-stripe" points="0,470 380,412 380,462 0,522" fill="var(--stripe-red)"/>
    </svg>
    <div class="runner-figure" role="img" aria-label="Blue silhouette of a running athlete"></div>
    <h1 class="brand-name">BRISK<br>COMET</h1>
    <p class="product-type">ENERGY SHOTS</p>
    <p class="product-details">2OZ BOTTLE<br>BERRY FLAVOR</p>
  </section>
</main>
</body>
</html>
```